Shopify store for hemp

I need a store designed for Shopify for my hemp company. I currently have a brick and mortar store, but we are looking to get some business online as well. I will upload our logo for reference. We want a clean look. Categories like THCA Flower, Concentrates, Vapes, Edibles would be nice so that we can put individual products under them. I want something about all products being third-party lab tested. All products are sourced in the United States.
Updates

Need extra days to review

Target Market(s)

Former customers who live in different areas and signed up for our marketing list.

Industry/Entity Type

Hemp/Cannabis

Coding

Coded - Design and coding required

Number of Pages Required

1 page

Requirements
Must have
• Clean feel

```html
<!DOCTYPE html>
<html lang="en">
<head>
<meta charset="utf-8">
<title>Summit Clearwater Dispensary</title>
<link href="https://fonts.googleapis.com/css2?family=Teko:wght@500;600&family=Inter:wght@400;500;600&display=swap" rel="stylesheet">
<style>
:root{
  --green:#4b8a4f;
  --green-dark:#3c7340;
  --green-deep:#2f5f33;
  --green-text:#4f8a52;
  --ink:#1f2a22;
  --muted:#3d453f;
  --line:#cfe0ef;
  --white:#ffffff;
  --faint:#f2f4f2;
}
*{box-sizing:border-box;margin:0;padding:0}
html,body{width:1200px;height:3810px;overflow:hidden}
body{font-family:"Inter",sans-serif;color:var(--ink);background:var(--white);position:relative}
.abs{position:absolute}
.display{font-family:"Teko",sans-serif;font-weight:600;line-height:1}

/* header */
.site-header{position:absolute;left:0;top:0;width:1200px;height:100px;background:var(--white);z-index:5}
.brand-badge{position:absolute;left:112px;top:6px;width:145px;height:145px;border-radius:50%;background:var(--white);box-shadow:0 4px 14px rgba(0,0,0,.18);display:flex;align-items:center;justify-content:center;text-align:center;font-weight:600;font-size:17px;color:var(--green-dark);line-height:1.2;z-index:6}
.main-nav{position:absolute;left:290px;top:38px;display:flex;gap:31px;font-size:15px;color:var(--ink)}
.main-nav .active{color:var(--green-text)}
.nav-caret{font-size:9px;margin-left:4px}
.btn{display:inline-flex;align-items:center;gap:14px;border-radius:30px;background:var(--white);font-size:15px;font-weight:500;color:var(--green-dark);height:45px;padding:0 14px 0 28px;box-shadow:0 3px 8px rgba(0,0,0,.12)}
.btn .dia{width:24px;height:24px;background:var(--green);transform:rotate(45deg);border-radius:3px;display:inline-block;margin:0 4px}
.btn-outline{border:1.5px solid #9fc3a2;box-shadow:0 3px 8px rgba(0,0,0,.08)}
.header-cta{position:absolute;left:888px;top:26px}

/* hero */
.hero{position:absolute;left:0;top:100px;width:1200px;height:590px;background:linear-gradient(180deg,#2d4a2f 0%,#3f6b3a 45%,#5a8a43 100%)}
.hero-title{position:absolute;left:111px;top:165px;font-size:72px;color:var(--white);letter-spacing:.5px;line-height:.88}
.hero-text{position:absolute;left:111px;top:318px;font-size:15px;line-height:26px;color:var(--white)}
.hero .btn{position:absolute;left:111px;top:392px}
.hero-product{position:absolute;left:740px;top:85px;width:350px;height:435px;border-radius:6px;background:linear-gradient(120deg,#e8efe6 0%,#2f6a4a 40%,#23593d 100%);opacity:.95}
.slide-arrow{position:absolute;width:34px;height:34px;background:var(--white);transform:rotate(45deg);border-radius:4px;display:flex;align-items:center;justify-content:center}
.slide-arrow svg{transform:rotate(-45deg)}
.notch{position:absolute;left:525px;width:150px;height:48px;background:var(--white);border-radius:75px 75px 0 0}
.notch .mark{position:absolute;left:55px;top:8px;width:40px;height:34px;border-radius:50% 50% 10% 10%;background:linear-gradient(#a8b93a,#6c8f2a)}

/* about */
.ghost{position:absolute;font-family:"Teko",sans-serif;font-weight:600;line-height:1;color:var(--faint);white-space:nowrap}
.section-title{font-size:48px;color:var(--green-text)}
.center{text-align:center}
.about-text{position:absolute;left:0;width:1200px;top:835px;font-size:15px;line-height:26px;color:var(--ink)}
.feature-card{position:absolute;top:920px;width:389px;height:265px;border:1.5px solid var(--line);border-radius:12px;background:var(--white)}
.feature-card .icon{position:absolute;left:36px;top:38px;width:70px;height:50px}
.feature-card h3{position:absolute;left:141px;top:40px;font-size:20px;font-weight:500;line-height:26px}
.feature-card p{position:absolute;left:36px;top:122px;width:330px;font-size:15px;line-height:26px;color:var(--ink)}
.feature-card .btn{position:absolute;left:36px;top:240px;height:45px}

/* green */
.green-band{position:absolute;left:0;top:1305px;width:1200px;height:1485px;background:linear-gradient(180deg,#4d8c51 0%,#468649 60%,#3f7d43 100%)}
.ghost-green{color:rgba(255,255,255,.07)}
.on-green{color:var(--white)}
.green-text{font-size:15px;line-height:26px;color:var(--white)}
.product-card{position:absolute;left:111px;top:1550px;width:979px;height:530px;border:1.5px solid rgba(255,255,255,.45);border-radius:14px}
.product-name{position:absolute;left:158px;top:1595px;font-size:46px;color:var(--white);text-decoration:underline;text-decoration-thickness:2px;text-underline-offset:6px}
.price{position:absolute;left:158px;top:1665px;color:var(--white)}
.price .big{font-size:70px}
.price .cur{font-size:44px}
.price .per{font-family:"Inter",sans-serif;font-size:20px;font-weight:400}
.checklist{position:absolute;left:160px;top:1830px;list-style:none;font-size:15px;color:var(--white)}
.checklist li{display:flex;align-items:center;gap:18px;height:40px}
.tick{width:22px;height:22px;border-radius:50%;background:var(--white);display:flex;align-items:center;justify-content:center}
.qty{position:absolute;left:160px;top:1974px;width:260px;height:44px;border:1.5px solid rgba(255,255,255,.7);border-radius:24px;display:flex;align-items:center;color:var(--white);font-size:16px}
.qty span{display:inline-block}
.plant{position:absolute;left:690px;top:1505px;width:510px;height:595px;border-radius:45% 40% 50% 45%;background:radial-gradient(circle at 50% 50%,#8fa54a 0%,#5f8a3a 45%,rgba(70,134,73,0) 72%)}
.cat{position:absolute;top:2367px;width:237px;height:289px;border-radius:6px;overflow:hidden;text-align:center;color:var(--white)}
.cat h4{position:absolute;left:0;right:0;top:195px;font-family:"Teko",sans-serif;font-weight:600;font-size:32px;line-height:1}
.cat span{position:absolute;left:0;right:0;top:236px;font-size:15px;font-weight:500}

/* testimonials */
.stars{position:absolute;left:537px;top:2898px;display:flex;gap:9px}
.review-card{position:absolute;left:390px;top:3003px;width:700px;height:334px;background:var(--white);border-radius:12px;box-shadow:0 10px 40px rgba(0,0,0,.08)}
.review-product{position:absolute;left:85px;top:2980px;width:310px;height:390px;border-radius:6px;background:linear-gradient(120deg,#e9efe7 0%,#2f6a4a 35%,#23593d 100%)}
.quote{position:absolute;left:487px;top:3128px;width:520px;font-size:15px;line-height:26px;font-style:italic;color:var(--ink)}
.author{position:absolute;left:487px;top:3252px;font-size:20px;color:var(--green-text)}
.dark-dia{position:absolute;width:32px;height:32px;background:var(--green-dark);transform:rotate(45deg);border-radius:3px;display:flex;align-items:center;justify-content:center}
.dark-dia svg{transform:rotate(-45deg)}

/* footer */
.site-footer{position:absolute;left:0;top:3467px;width:1200px;height:343px;background:var(--green)}
.footer-badge{position:absolute;left:540px;top:50px;width:120px;height:120px;border-radius:50%;background:var(--white);display:flex;align-items:center;justify-content:center;text-align:center;font-size:14px;font-weight:600;color:var(--green-dark);line-height:1.2}
.footer-nav{position:absolute;left:0;width:1200px;top:188px;display:flex;justify-content:center;gap:34px;font-size:17px;color:var(--white)}
.social{position:absolute;left:534px;top:250px;display:flex;gap:14px}
.social span{width:22px;height:22px;border-radius:50%;background:var(--white)}
.copyright{position:absolute;left:0;width:1200px;top:306px;text-align:center;font-size:12px;color:var(--white)}
</style>
</head>
<body>

<header class="site-header">
  <div class="brand-badge">Summit<br>Clearwater</div>
  <nav class="main-nav">
    <span class="active">Home</span><span>Products</span><span>About</span><span>Categories<span class="nav-caret">▼</span></span><span>Testimonials</span><span>Contact</span>
  </nav>
  <a class="btn btn-outline header-cta">Get in Touch <i class="dia"></i></a>
</header>

<section class="hero" role="img" aria-label="Photo of a hemp field with forest behind it">
  <h1 class="display hero-title">Premium Hemp Products<br>Trusted and Tested</h1>
  <p class="hero-text">We are committed to delivering premium hemp products sourced<br>exclusively in the United States.</p>
  <a class="btn">Shop Now <i class="dia"></i></a>
  <div class="hero-product" role="img" aria-label="CBD oil bottle and box product mockup"></div>
  <div class="slide-arrow" style="left:38px;top:373px"><svg width="16" height="16" viewBox="0 0 16 16"><path d="M13 8H3M7 4 3 8l4 4" stroke="#4b8a4f" stroke-width="1.8" fill="none"/></svg></div>
  <div class="slide-arrow" style="left:1128px;top:373px"><svg width="16" height="16" viewBox="0 0 16 16"><path d="M3 8h10M9 4l4 4-4 4" stroke="#4b8a4f" stroke-width="1.8" fill="none"/></svg></div>
</section>
<div class="notch" style="top:642px"><span class="mark" role="img" aria-label="Hemp leaf emblem"></span></div>

<div class="ghost" style="left:0;top:735px;font-size:215px">ABOUT</div>
<h2 class="display section-title abs center" style="left:0;width:1200px;top:765px">Who We Are</h2>
<p class="about-text center">At Summit Clearwater, we are committed to delivering premium hemp products and<br>we believe in transparency and trust, ensuring customers receive products they can rely on.</p>

<article class="feature-card" style="left:205px">
  <svg class="icon" viewBox="0 0 70 50"><path d="M4 8h58l4 10-6 18-14 8-10-6H18L6 30z" fill="none" stroke="#4b8a4f" stroke-width="2"/><path d="M10 16h22M10 22h30M12 28h34" stroke="#4b8a4f" stroke-width="1.6"/></svg>
  <h3>All Products are<br>Sourced in the USA</h3>
  <p>We partner with trusted U.S. hemp farms and manufacturers dedicated to sustainable and ethical practices.</p>
  <a class="btn btn-outline">Learn More <i class="dia"></i></a>
</article>
<article class="feature-card" style="left:606px">
  <svg class="icon" viewBox="0 0 70 50" style="left:36px;top:34px;height:60px"><circle cx="38" cy="18" r="10" fill="none" stroke="#4b8a4f" stroke-width="2"/><path d="M20 6l8 8M8 44h40M14 44V30h16M44 34a12 12 0 0 1-20 8" fill="none" stroke="#4b8a4f" stroke-width="2"/></svg>
  <h3>All Products are<br>Third-Party Lab Tested</h3>
  <p>We partner with trusted U.S. hemp farms and manufacturers dedicated to sustainable and ethical practices.</p>
  <a class="btn btn-outline">Learn More <i class="dia"></i></a>
</article>

<section class="green-band"></section>
<div class="ghost ghost-green" style="left:530px;top:1330px;font-size:210px">PRODUCT</div>
<h2 class="display abs on-green" style="left:111px;top:1380px;font-size:48px">Our Featured Products</h2>
<p class="abs green-text" style="left:111px;top:1448px">Discover our top-quality hemp products, all third-party lab tested for purity and potency.<br>Browse through our selection and add your favorites to the cart with ease.</p>

<div class="product-card"></div>
<div class="plant" role="img" aria-label="Close-up photo of a THCA flower bud with leaves"></div>
<h3 class="display product-name">Verdant Peak THCA Flower</h3>
<div class="display price"><span class="cur">$</span><span class="big">36.99</span><span class="per">/per batch</span></div>
<p class="abs green-text" style="left:160px;top:1752px">Verdant Peak THCA Flower is a carefully cultivated strain known for its dense,<br>crystalline buds and rich terpene profile offering notes of citrus and pine.</p>
<ul class="checklist">
  <li><span class="tick"><svg width="12" height="12" viewBox="0 0 12 12"><path d="M2 6l3 3 5-6" stroke="#4b8a4f" stroke-width="2" fill="none"/></svg></span>Third-Party Lab Tested</li>
  <li><span class="tick"><svg width="12" height="12" viewBox="0 0 12 12"><path d="M2 6l3 3 5-6" stroke="#4b8a4f" stroke-width="2" fill="none"/></svg></span>Sourced in the USA</li>
  <li><span class="tick"><svg width="12" height="12" viewBox="0 0 12 12"><path d="M2 6l3 3 5-6" stroke="#4b8a4f" stroke-width="2" fill="none"/></svg></span>Transparent Lab Results</li>
</ul>
<div class="qty">
  <span style="margin-left:20px">+</span><span style="margin-left:24px;font-size:20px;font-weight:600">2</span><span style="margin-left:24px">–</span>
  <span style="margin-left:22px;height:44px;border-left:1.5px solid rgba(255,255,255,.7)"></span>
  <span style="margin-left:20px;font-size:15px;font-weight:600">Add To Cart</span>
</div>
<a class="btn abs" style="left:430px;top:1974px;height:44px">Buy Now <i class="dia"></i></a>
<div class="slide-arrow" style="left:38px;top:1802px"><svg width="16" height="16" viewBox="0 0 16 16"><path d="M13 8H3M7 4 3 8l4 4" stroke="#4b8a4f" stroke-width="1.8" fill="none"/></svg></div>
<div class="slide-arrow" style="left:1128px;top:1802px"><svg width="16" height="16" viewBox="0 0 16 16"><path d="M3 8h10M9 4l4 4-4 4" stroke="#4b8a4f" stroke-width="1.8" fill="none"/></svg></div>

<div class="ghost ghost-green" style="left:0;top:2165px;font-size:215px">SHOP</div>
<h2 class="display abs on-green center" style="left:0;width:1200px;top:2185px;font-size:48px">Shop by Categories</h2>
<p class="abs green-text center" style="left:0;width:1200px;top:2270px">Discover our top-quality hemp products, all third-party lab tested for purity and potency.<br>Browse through our collections and selection and add shop what you need with ease.</p>

<a class="cat" style="left:111px;background:linear-gradient(180deg,#7b8d4a 0%,#4f6a2e 55%,#1f2a18 100%)" role="img" aria-label="Photo of a THCA flower bud"><h4>THCA FLOWERS</h4><span>View Products</span></a>
<a class="cat" style="left:358px;background:linear-gradient(180deg,#6a4a20 0%,#e2a21c 45%,#3a2a10 100%)" role="img" aria-label="Photo of amber hemp concentrate in a jar"><h4>CONCENTRATES</h4><span>View Products</span></a>
<a class="cat" style="left:606px;background:linear-gradient(180deg,#d8d8d6 0%,#8d8d8a 55%,#2a2a28 100%)" role="img" aria-label="Photo of a metal vape cartridge"><h4>ORGANIC VAPES</h4><span>View Products</span></a>
<a class="cat" style="left:853px;background:linear-gradient(180deg,#f4c65a 0%,#d89322 55%,#5a3a12 100%)" role="img" aria-label="Photo of hemp gummies on a spoon"><h4>HEMP EDIBLES</h4><span>View Products</span></a>

<div class="notch" style="top:2742px"><span class="mark" role="img" aria-label="Hemp leaf emblem"></span></div>

<h2 class="display section-title abs" style="left:111px;top:2885px">Our Client Testimonials</h2>
<div class="stars">
  <svg width="18" height="18" viewBox="0 0 20 20"><path d="M10 1l2.6 6 6.4.6-4.9 4.3 1.5 6.4L10 15l-5.6 3.3 1.5-6.4L1 7.6 7.4 7z" fill="#4b8a4f"/></svg>
  <svg width="18" height="18" viewBox="0 0 20 20"><path d="M10 1l2.6 6 6.4.6-4.9 4.3 1.5 6.4L10 15l-5.6 3.3 1.5-6.4L1 7.6 7.4 7z" fill="#4b8a4f"/></svg>
  <svg width="18" height="18" viewBox="0 0 20 20"><path d="M10 1l2.6 6 6.4.6-4.9 4.3 1.5 6.4L10 15l-5.6 3.3 1.5-6.4L1 7.6 7.4 7z" fill="#4b8a4f"/></svg>
  <svg width="18" height="18" viewBox="0 0 20 20"><path d="M10 1l2.6 6 6.4.6-4.9 4.3 1.5 6.4L10 15l-5.6 3.3 1.5-6.4L1 7.6 7.4 7z" fill="#4b8a4f"/></svg>
  <svg width="18" height="18" viewBox="0 0 20 20"><path d="M10 1l2.6 6 6.4.6-4.9 4.3 1.5 6.4L10 15l-5.6 3.3 1.5-6.4L1 7.6 7.4 7z" fill="#4b8a4f"/></svg>
</div>
<div class="review-card"></div>
<div class="ghost" style="left:440px;top:3045px;font-size:175px">REVIEWS</div>
<div class="review-product" role="img" aria-label="CBD oil bottle and box product mockup"></div>
<h3 class="display abs" style="left:487px;top:3078px;font-size:40px;color:var(--green-text)">Trusted Quality, Exceptional Results</h3>
<p class="quote">"Since discovering these hemp products, my wellness routine has never been better. The quality is unmatched, and I appreciate the transparency with lab testing. Highly recommend for anyone seeking reliable and some effective hemp solutions."</p>
<p class="author">– Daniel R. Hollis</p>
<div class="dark-dia" style="left:904px;top:3248px"><svg width="14" height="14" viewBox="0 0 16 16"><path d="M13 8H3M7 4 3 8l4 4" stroke="#fff" stroke-width="1.8" fill="none"/></svg></div>
<div class="dark-dia" style="left:963px;top:3248px"><svg width="14" height="14" viewBox="0 0 16 16"><path d="M3 8h10M9 4l4 4-4 4" stroke="#fff" stroke-width="1.8" fill="none"/></svg></div>

<footer class="site-footer">
  <div class="ghost" style="left:15px;top:25px;font-size:150px;color:rgba(255,255,255,.08)">SUMMIT CLEARWATER</div>
  <div class="footer-badge">Summit<br>Clearwater</div>
  <nav class="footer-nav"><span>Home</span><span>Products</span><span>About</span><span>Categories</span><span>Testimonials</span><span>Contact</span></nav>
  <div class="social"><span></span><span></span><span></span><span></span></div>
  <p class="copyright">© 2025 Summit Clearwater Dispensary. All Rights Reserved.</p>
</footer>

</body>
</html>
```